Valdemora Tree Experts LLC company flyer

I need a flyer with information and photos about the tree trimming and removal services I provide. I want it to be elegant and organic. Include photos of my work that capture the essence, complexity and professionalism of my work. I want it to include information about the services we provide and information on why it is important to contract a certified arborist to manage your trees. I need it to be in Spanish as it is for Puerto Rico. Services we provide: especialistas en podas y remociones controladas de árboles y palmas, evaluaciones de riesgo de árboles, limpieza de palmas, transplante y siembra de árboles y palmas, arboristas certificados por la Consejo Mundial de Jardinería Técnica (CMJ). Contamos con Seguro de Responsabilidad Pública y ORT.

Target Market(s)

Homeowners, company owners, nest hop owners, hotels, restaurants,

Industry/Entity Type

Arboriculture

Requirements
Must have
• My CMJ Certified Arborist logo

```html
<!DOCTYPE html>
<html lang="es">
<head>
<meta charset="utf-8">
<title>Valdemora Tree Experts LLC</title>
<link rel="stylesheet" href="https://fonts.googleapis.com/css2?family=Anton&family=Poppins:wght@400;500;600;700;800&display=swap">
<style>
:root{
  --green-light:#8a9c17;
  --green-mid:#5d6d12;
  --green-dark:#3a4511;
  --green-deep:#2a320d;
  --ink:#2e2e2e;
  --gold:#d9c77c;
  --paper:#ffffff;
  --sky:#e8eef5;
}
*{margin:0;padding:0;box-sizing:border-box}
html,body{width:858px;height:1200px;overflow:hidden;background:var(--paper)}
body{font-family:'Poppins',sans-serif;color:var(--ink)}
.flyer{position:relative;width:858px;height:1200px;overflow:hidden;background:var(--paper)}
.hero-photo{position:absolute;left:620px;top:0;width:238px;height:720px;background:linear-gradient(180deg,#3d5a2a 0%,#5c7a3e 45%,#cfdbe6 80%,#f4f6f9 100%)}
.hero-shape{position:absolute;left:0;top:0}
.climber-photo{position:absolute;left:290px;top:0;width:300px;height:220px;border-radius:0 0 140px 40px;background:radial-gradient(ellipse at 55% 45%,rgba(120,92,60,.55),rgba(138,156,23,0) 70%)}
.photo-circle{position:absolute;border-radius:50%;border:4px solid var(--paper);box-shadow:0 0 0 3px var(--green-deep)}
.photo-circle.one{left:582px;top:58px;width:200px;height:200px;background:linear-gradient(160deg,#6f9bd6,#4f7a3a 65%,#2f4a1f)}
.photo-circle.two{left:505px;top:300px;width:196px;height:196px;background:linear-gradient(180deg,#e9edf0 0%,#dfe3e6 48%,#5b7a34 62%,#3b4d1f 100%)}
.photo-circle.three{left:356px;top:503px;width:180px;height:180px;background:linear-gradient(150deg,#4f6f2c,#8a7a5a 55%,#3a4a20)}
.brand{position:absolute;left:40px;top:40px;width:280px;text-align:center}
.brand-mark{width:112px;height:112px;margin:0 auto 22px;border-radius:50%;border:3px solid var(--green-deep);background:#efe9cf}
.brand-name{font-weight:600;font-size:15px;letter-spacing:2px;color:var(--green-deep)}
.brand-tag{font-weight:600;font-size:7.5px;letter-spacing:4px;color:var(--green-deep);margin-top:4px}
.tagline-band{position:absolute;left:0;top:316px;width:393px;height:34px;background:var(--green-deep);border:2px solid var(--paper);border-left:none;border-radius:0 18px 18px 0;color:#fff;font-weight:500;font-size:19px;letter-spacing:8.5px;line-height:30px;padding-left:46px}
.headline{position:absolute;left:46px;top:362px;color:#fff;text-transform:uppercase}
.headline .line-a{font-family:'Anton',sans-serif;font-size:41px;line-height:46px;letter-spacing:-.3px}
.headline .line-b{font-family:'Anton',sans-serif;font-size:68px;line-height:80px;letter-spacing:-.5px}
.headline .line-c{font-weight:700;font-size:31px;line-height:40px}
.rule{position:absolute;left:48px;top:529px;width:42px;height:4px;border-radius:2px;background:var(--green-deep)}
.intro{position:absolute;left:48px;top:546px;width:260px;color:#fff;font-size:16.5px;line-height:20px}
.services{position:absolute;left:48px;top:700px;width:352px}
.services h2{font-weight:400;font-size:27px;color:var(--ink);display:flex;align-items:center;gap:12px}
.services h2 b{font-weight:700;color:var(--green-dark)}
.services h2 .arrow{flex:1;height:2px;background:var(--green-dark);position:relative}
.services h2 .arrow::after{content:"";position:absolute;right:-2px;top:-3px;width:7px;height:7px;border-radius:50%;background:var(--green-dark)}
.service-list{list-style:none;margin-top:16px}
.service-list li{display:flex;align-items:center;gap:9px;height:33px;margin-bottom:7.5px;font-size:14.5px;font-weight:500}
.service-list svg{flex:none}
.divider{position:absolute;left:426px;top:706px;width:2px;height:208px;background:linear-gradient(180deg,rgba(0,0,0,0),#cfcfcf 20%,#cfcfcf 80%,rgba(0,0,0,0))}
.badge{position:absolute;left:458px;width:116px;text-align:center}
.badge .num{font-family:'Anton',sans-serif;color:var(--green-deep);line-height:1}
.badge .ribbon{display:inline-block;background:var(--gold);color:var(--green-deep);font-weight:700;font-size:8px;letter-spacing:1.5px;padding:3px 12px;border-radius:2px}
.badge.years{top:712px}
.badge.years .num{font-size:46px}
.badge.years .script{font-style:italic;font-size:13px;color:var(--green-deep);margin-top:-4px}
.badge.best{top:820px}
.badge.best .num{font-size:34px;margin-top:6px}
.badge.best .stars{color:#e8c33e;font-size:11px;letter-spacing:2px}
.fact{position:absolute;left:592px;width:210px;font-size:15.5px;line-height:18px;font-weight:500;color:var(--ink)}
.fact b{color:var(--green-dark);font-weight:700}
.fact.years{top:715px}
.fact.best{top:827px}
.dash{position:absolute;left:462px;top:806px;width:340px;border-top:1.5px dashed #555}
.standards{position:absolute;left:48px;top:1028px;width:230px;font-size:10.2px;line-height:12.2px;color:var(--ink)}
.cert{position:absolute;top:1028px;width:62px;height:116px;background:var(--green-mid);border:3px solid #2f6b35;outline:1px solid #2f6b35;outline-offset:2px}
.cert.a{left:288px}
.cert.b{left:352px;background:#3e7d3c}
.contact-band{position:absolute;left:440px;top:1019px;width:374px;height:36px;background:var(--green-deep);border-radius:0 18px 18px 0;border-left:4px solid var(--green-deep);box-shadow:-6px 0 0 -2px var(--paper),-8px 0 0 -2px var(--green-deep);color:#fff;font-weight:700;font-size:14.5px;line-height:36px;padding-left:16px}
.contact{position:absolute;left:448px;top:1068px}
.contact .row{display:flex;align-items:center;gap:9px}
.contact .phone{font-weight:700;font-size:19px;height:28px}
.contact .email{font-size:14px;height:24px}
.closing{position:absolute;left:448px;top:1126px;font-weight:800;font-size:14px;color:var(--green-deep)}
.closing span{color:var(--green-mid)}
</style>
</head>
<body>
<main class="flyer">
  <div class="hero-photo" role="img" aria-label="Foto de arborista certificado descendiendo con cuerdas desde la copa de un árbol grande"></div>

  <svg class="hero-shape" width="858" height="720" viewBox="0 0 858 720" aria-hidden="true">
    <defs>
      <linearGradient id="heroGreen" x1="0" y1="0" x2="0" y2="1">
        <stop offset="0" stop-color="#8a9c17"/>
        <stop offset=".55" stop-color="#5d6d12"/>
        <stop offset="1" stop-color="#3a4511"/>
      </linearGradient>
    </defs>
    <path d="M0 0 H688 C664 210 560 520 330 610 C210 655 80 640 0 622 Z" fill="url(#heroGreen)"/>
    <path d="M0 630 C90 650 220 664 340 622" fill="none" stroke="#2a320d" stroke-width="3"/>
    <path d="M0 624 C90 644 220 658 340 616" fill="none" stroke="#ffffff" stroke-width="3"/>
  </svg>

  <div class="climber-photo" role="img" aria-label="Foto de arborista con casco y motosierra trabajando sobre una rama"></div>

  <div class="photo-circle one" role="img" aria-label="Foto de arborista trepando entre las ramas de un árbol"></div>
  <div class="photo-circle two" role="img" aria-label="Foto de ramas cortadas frente a una casa tras una remoción"></div>
  <div class="photo-circle three" role="img" aria-label="Foto de arborista cortando un tronco con motosierra"></div>

  <header class="brand">
    <div class="brand-mark"></div>
    <div class="brand-name">VALDEMORA TREE EXPERTS</div>
    <div class="brand-tag">MANEJO DE ARBOLES</div>
  </header>

  <div class="tagline-band">ESPECIALISTAS EN</div>

  <h1 class="headline">
    <div class="line-a">Podas y Remociones</div>
    <div class="line-b">Técnicas de</div>
    <div class="line-c">Árboles y Palmas</div>
  </h1>
  <div class="rule"></div>
  <p class="intro">Somos una compañía especializada en el manejo de árboles y palmas</p>

  <section class="services">
    <h2>OUR <b>SERVICES</b><span class="arrow"></span></h2>
    <ul class="service-list">
      <li><svg width="34" height="34" viewBox="0 0 34 34"><circle cx="17" cy="17" r="16" fill="#3a4511" stroke="#c9cfb3" stroke-width="1.5"/><path d="M12 23 L22 11 M20 11 h3 v3" stroke="#fff" stroke-width="1.6" fill="none"/></svg>Poda de árboles</li>
      <li><svg width="34" height="34" viewBox="0 0 34 34"><circle cx="17" cy="17" r="16" fill="#3a4511" stroke="#c9cfb3" stroke-width="1.5"/><path d="M11 23 L23 11 M11 11 L23 23" stroke="#fff" stroke-width="1.6"/></svg>Poda de árboles</li>
      <li><svg width="34" height="34" viewBox="0 0 34 34"><circle cx="17" cy="17" r="16" fill="#3a4511" stroke="#c9cfb3" stroke-width="1.5"/><path d="M17 9 L24 12 V17 C24 21 21 24 17 25 C13 24 10 21 10 17 V12 Z" stroke="#fff" stroke-width="1.5" fill="none"/><path d="M14 17 h6 M17 14 v6" stroke="#fff" stroke-width="1.5"/></svg>Prevención y control de enfermedades.</li>
      <li><svg width="34" height="34" viewBox="0 0 34 34"><circle cx="17" cy="17" r="16" fill="#3a4511" stroke="#c9cfb3" stroke-width="1.5"/><path d="M17 10 L25 24 H9 Z" stroke="#fff" stroke-width="1.5" fill="none"/><path d="M17 15 v4 M17 21 v1" stroke="#fff" stroke-width="1.6"/></svg>Servicio de árboles de emergencia</li>
      <li><svg width="34" height="34" viewBox="0 0 34 34"><circle cx="17" cy="17" r="16" fill="#3a4511" stroke="#c9cfb3" stroke-width="1.5"/><circle cx="17" cy="17" r="7" stroke="#fff" stroke-width="1.5" fill="none"/><path d="M17 13 v4 l3 2" stroke="#fff" stroke-width="1.5" fill="none"/></svg>Mantenimiento regular de los árboles</li>
    </ul>
  </section>

  <div class="divider"></div>

  <div class="badge years">
    <div class="num">15</div>
    <div class="script">Year</div>
    <div class="ribbon">EXPERIENCE</div>
  </div>
  <p class="fact years">Contamos con más de <b>15 años</b> de experiencia en la industria de la Arboricultura.</p>

  <div class="dash"></div>

  <div class="badge best">
    <div class="num">BEST</div>
    <div class="stars">★★★</div>
    <div class="ribbon">DISPOSICIÓN</div>
  </div>
  <p class="fact best">Estamos a la mejor disposición de servirles.</p>

  <p class="standards">Realizamos podas y remociones técnicas siguiendo los más altos estándares del Consejo Mundial de Jardinería Técnica (CMJ) y los estándares de seguridad del Instituto Nacional de Normas Técnicas para operaciones de Arboricultura (INNT Z133).</p>
  <div class="cert a" role="img" aria-label="Sello de arborista certificado CMJ"></div>
  <div class="cert b" role="img" aria-label="Sello de miembro del CMJ"></div>

  <div class="contact-band">CONTACT US TO SEE HOW WE CAN HELP YOU</div>
  <div class="contact">
    <div class="row phone"><svg width="16" height="16" viewBox="0 0 16 16"><circle cx="8" cy="8" r="7.5" fill="#3a4511"/><path d="M5 4.5 C5 9 7 11 11.5 11.5 L12 10 L10 9 L9 10 C7.5 9.5 6.5 8.5 6 7 L7 6 L6 4 Z" fill="#fff"/></svg>787-555-0142</div>
    <div class="row email"><svg width="16" height="12" viewBox="0 0 16 12"><rect x="1" y="1" width="14" height="10" fill="#3a4511"/><path d="M1 1 L8 7 L15 1" stroke="#fff" stroke-width="1.2" fill="none"/></svg>arbolesvaldemora@correo.com</div>
  </div>
  <p class="closing"><span>QUOTES ARE FREE.</span> WE WORK THE ENTIRE ISLAND.</p>
</main>
</body>
</html>
```